Modern looking signage for dental office.

Exterior signage for passing cars
Target Market(s)
Cars passing by
Font styles to use
Sans Serif
Colors
3276b5
Requirements
Must have
- Logo
- OPEN ON SUTURDAY AND SUNDAY
- NIGHT CLINIC AVAILABLE
- PLEASE USE THE FONT TYPE IN FILE 4 UPLOADED BELOW.
- (482) 730-2964
- Modern looking

```html
<!DOCTYPE html>
<html lang="en">
<head>
<meta charset="utf-8">
<title>Nova Dental – Exterior Sign</title>
<link href="https://fonts.googleapis.com/css2?family=Carlito:wght@400;700&display=swap" rel="stylesheet">
<style>
  :root {
    --brand-blue: #3276b5;
    --ink-grey: #4a4a4c;
    --line-grey: #5a5a5c;
    --sign-white: #ffffff;
    --backdrop: #e9eaec;
  }
  html, body {
    margin: 0;
    padding: 0;
    width: 1200px;
    height: 800px;
    overflow: hidden;
    background: var(--backdrop);
    font-family: "Carlito", "Calibri", sans-serif;
  }
  .sign {
    position: absolute;
    left: 280px;
    top: 30px;
    width: 640px;
    height: 740px;
    background: var(--sign-white);
    box-shadow: 0 6px 24px rgba(0,0,0,0.18);
    overflow: hidden;
  }
  .sign__band {
    position: absolute;
    left: 0;
    top: 0;
    width: 640px;
    height: 740px;
  }
  .brand {
    position: absolute;
    left: 0;
    top: 50px;
    width: 100%;
    text-align: center;
    color: var(--ink-grey);
  }
  .brand__mark {
    display: block;
    width: 118px;
    height: 118px;
    margin: 0 auto;
    border: 2px solid var(--ink-grey);
    border-radius: 50%;
    box-sizing: border-box;
  }
  .brand__name {
    margin: 26px 0 0;
    font-size: 70px;
    font-weight: 400;
    letter-spacing: 2px;
    line-height: 1;
    white-space: nowrap;
  }
  .brand__tagline {
    margin: 14px 0 0;
    font-size: 24px;
    font-weight: 400;
    letter-spacing: 0.5px;
    line-height: 1;
    white-space: nowrap;
  }
  .hours {
    position: absolute;
    left: 0;
    top: 405px;
    width: 100%;
    text-align: center;
    color: var(--sign-white);
    font-weight: 700;
    font-size: 40px;
    line-height: 52px;
    letter-spacing: -0.5px;
    white-space: nowrap;
  }
  .hours p { margin: 0; }
  .contact {
    position: absolute;
    left: 0;
    top: 588px;
    width: 100%;
    text-align: center;
    color: var(--ink-grey);
  }
  .contact__icon {
    display: block;
    width: 56px;
    height: 56px;
    margin: 0 auto;
  }
  .contact__phone {
    margin: 12px 0 0;
    font-size: 56px;
    font-weight: 400;
    line-height: 1;
    white-space: nowrap;
  }
</style>
</head>
<body>
  <main class="sign">
    <svg class="sign__band" viewBox="0 0 640 740" aria-hidden="true">
      <path d="M0 318 Q320 392 640 318" fill="none" stroke="var(--line-grey)" stroke-width="3"/>
      <path d="M0 330 Q320 400 640 330 L640 612 Q320 482 0 612 Z" fill="var(--brand-blue)"/>
      <path d="M0 626 Q320 494 640 620" fill="none" stroke="var(--line-grey)" stroke-width="3"/>
    </svg>

    <header class="brand">
      <span class="brand__mark"></span>
      <h1 class="brand__name">NOVA DENTAL</h1>
      <p class="brand__tagline">MODERN GENERAL DENTISTRY</p>
    </header>

    <section class="hours">
      <p>OPEN ON SUTURDAY AND SUNDAY</p>
      <p>NIGHT CLINIC AVAILABLE</p>
    </section>

    <footer class="contact">
      <svg class="contact__icon" viewBox="0 0 64 64" aria-hidden="true">
        <circle cx="32" cy="32" r="30" fill="none" stroke="var(--ink-grey)" stroke-width="2"/>
        <path d="M22 18 l6 -2 l5 9 l-4 4 q3 7 10 10 l4 -4 l9 5 l-2 6 q-4 4 -10 2 q-16 -6 -21 -21 q-1 -6 3 -9 Z"
              fill="none" stroke="var(--brand-blue)" stroke-width="2.4" stroke-linejoin="round"/>
      </svg>
      <p class="contact__phone">(482) 730-2964</p>
    </footer>
  </main>
</body>
</html>
```